Wedding Marlies & Joost - Save the Date Wedding Card

I would like to have a creative save the date wedding card. We like grey/black/white colors and modern/ plain and simple.
I like the Save the Date copy big and book a flight copy smaller. I like stylish fonts for the save the date copy
Copy front:
Save the Date & book a flight
7-10-2017 Denia (Spanje)
Marlies & Joost
Onze dag is niet compleet zonder jou!
Copy back:
6-10 preferred travel date
7-10 wedding ceremony/drinks/dinner/party
8-10 hangover breakfast
Nearest Airports Valencia & Alicante
More info will be available soon!
wedding guests
Wedding

```html
<!DOCTYPE html>
<html lang="nl">
<head>
<meta charset="utf-8">
<title>Save the Date – Marlies &amp; Joost</title>
<link href="https://fonts.googleapis.com/css2?family=Amatic+SC:wght@700&family=Dancing+Script:wght@700&family=Kaushan+Script&display=swap" rel="stylesheet">
<style>
  :root {
    --backdrop: #ecdfe0;
    --paper: #ffffff;
    --ink: #111111;
    --silver: #c4c4c4;
    --ribbon: #bdbdbd;
    --shadow: rgba(60, 40, 45, 0.35);
    --font-caps: "Amatic SC", sans-serif;
    --font-title: "Kaushan Script", cursive;
    --font-list: "Dancing Script", cursive;
  }
  * { margin: 0; padding: 0; box-sizing: border-box; }
  html, body {
    width: 1200px; height: 924px; overflow: hidden;
    background: var(--backdrop);
  }
  .stage { position: relative; width: 1200px; height: 924px; }

  .card {
    position: absolute; width: 426px; height: 427px;
    background: var(--paper); color: var(--ink);
    box-shadow: 4px 6px 10px var(--shadow);
    overflow: hidden;
  }
  .card--front { left: 118px; top: 252px; }
  .card--back-light { left: 650px; top: 22px; }
  .card--back-dark { left: 650px; top: 472px; background: var(--ink); color: var(--paper); }

  .card__art { position: absolute; inset: 0; width: 426px; height: 427px; }

  .line { position: absolute; left: 0; width: 100%; text-align: center; white-space: nowrap; }

  /* front */
  .couple { top: 76px; font-family: var(--font-caps); font-size: 24px; }
  .title { font-family: var(--font-title); line-height: 1; text-shadow: 3px 3px 0 var(--silver); }
  .title--save { top: 98px; font-size: 52px; left: -6px; }
  .title--date { top: 196px; font-size: 80px; left: 6px; }
  .ribbon-text {
    top: 162px; font-family: var(--font-caps); font-size: 34px;
    letter-spacing: 1px; transform: rotate(-3deg);
  }
  .when { top: 322px; font-family: var(--font-caps); font-size: 26px; }
  .tagline { top: 352px; font-family: var(--font-caps); font-size: 26px; letter-spacing: 0.5px; }

  /* back */
  .schedule { position: absolute; left: 70px; top: 112px; font-family: var(--font-list); font-size: 25px; line-height: 29px; }
  .schedule__row { display: flex; white-space: nowrap; }
  .schedule__day { width: 64px; }
  .schedule__dot { width: 20px; }
  .schedule__row--cont { padding-left: 84px; }
  .airports { top: 244px; font-family: var(--font-caps); font-size: 25px; }
  .more-info { top: 278px; font-family: var(--font-caps); font-size: 20px; }
</style>
</head>
<body>
<main class="stage">

  <!-- front -->
  <section class="card card--front">
    <svg class="card__art" viewBox="0 0 426 427">
      <circle role="img" aria-label="Leafy wreath ornament" cx="192" cy="170" r="122" fill="none" stroke="var(--ink)" stroke-width="12"/>
      <rect role="img" aria-label="Corner flourish ornament" x="58" y="26" width="72" height="52" rx="22" fill="var(--ink)"/>
      <rect role="img" aria-label="Corner flourish ornament" x="254" y="26" width="72" height="52" rx="22" fill="var(--ink)"/>
      <rect role="img" aria-label="Corner flourish ornament" x="58" y="250" width="72" height="52" rx="22" fill="var(--ink)"/>
      <rect role="img" aria-label="Corner flourish ornament" x="254" y="250" width="72" height="52" rx="22" fill="var(--ink)"/>
      <polygon class="ribbon-tail" points="22,152 70,150 70,186 30,190 44,170" fill="var(--ribbon)"/>
      <polygon class="ribbon-tail" points="326,140 402,134 386,156 406,170 330,178" fill="var(--ribbon)"/>
      <polygon class="ribbon-fold" points="86,186 104,196 104,180" fill="var(--ink)"/>
      <polygon class="ribbon-fold" points="308,172 290,180 290,164" fill="var(--ink)"/>
      <polygon class="ribbon-band" points="60,164 330,148 334,186 64,202" fill="var(--ribbon)"/>
    </svg>
    <p class="line couple">Marlies &amp; Joost</p>
    <h1 class="line title title--save">Save the</h1>
    <p class="line ribbon-text">And book a flight</p>
    <p class="line title title--date">Date</p>
    <p class="line when">7 oct 2017 • Denia (Spanje)</p>
    <p class="line tagline">Onze dag is niet compleet zonder jou!</p>
  </section>

  <!-- back, light -->
  <section class="card card--back-light">
    <svg class="card__art" viewBox="0 0 426 427">
      <circle role="img" aria-label="Leafy wreath ornament" cx="218" cy="212" r="188" fill="none" stroke="var(--ink)" stroke-width="10"/>
      <rect role="img" aria-label="Corner flourish ornament" x="18" y="344" width="74" height="52" rx="22" fill="var(--ink)"/>
      <rect role="img" aria-label="Corner flourish ornament" x="336" y="344" width="74" height="52" rx="22" fill="var(--ink)"/>
      <g class="divider" stroke="var(--ink)" stroke-width="1.5">
        <line x1="132" y1="94" x2="294" y2="94"/>
        <line x1="132" y1="330" x2="294" y2="330"/>
      </g>
      <rect role="img" aria-label="Small scroll ornament" x="200" y="88" width="26" height="12" rx="6" fill="var(--ink)"/>
      <rect role="img" aria-label="Small scroll ornament" x="200" y="324" width="26" height="12" rx="6" fill="var(--ink)"/>
    </svg>
    <div class="schedule">
      <p class="schedule__row"><span class="schedule__day">6-10</span><span class="schedule__dot">•</span><span>preferred travel date</span></p>
      <p class="schedule__row"><span class="schedule__day">7-10</span><span class="schedule__dot">•</span><span>wedding ceremony</span></p>
      <p class="schedule__row schedule__row--cont">drinks / dinner / party</p>
      <p class="schedule__row"><span class="schedule__day">8-10</span><span class="schedule__dot">•</span><span>hangover breakfast</span></p>
    </div>
    <p class="line airports">Nearest Airports Valencia &amp; Alicante</p>
    <p class="line more-info">More info will be available soon!</p>
  </section>

  <!-- back, dark -->
  <section class="card card--back-dark">
    <svg class="card__art" viewBox="0 0 426 427">
      <circle role="img" aria-label="Leafy wreath ornament" cx="218" cy="212" r="188" fill="none" stroke="var(--silver)" stroke-width="10"/>
      <rect role="img" aria-label="Corner flourish ornament" x="18" y="344" width="74" height="52" rx="22" fill="var(--silver)"/>
      <rect role="img" aria-label="Corner flourish ornament" x="336" y="344" width="74" height="52" rx="22" fill="var(--silver)"/>
      <g class="divider" stroke="var(--silver)" stroke-width="1.5">
        <line x1="132" y1="94" x2="294" y2="94"/>
        <line x1="132" y1="330" x2="294" y2="330"/>
      </g>
      <rect role="img" aria-label="Small scroll ornament" x="200" y="88" width="26" height="12" rx="6" fill="var(--silver)"/>
      <rect role="img" aria-label="Small scroll ornament" x="200" y="324" width="26" height="12" rx="6" fill="var(--silver)"/>
    </svg>
    <div class="schedule">
      <p class="schedule__row"><span class="schedule__day">6-10</span><span class="schedule__dot">•</span><span>preferred travel date</span></p>
      <p class="schedule__row"><span class="schedule__day">7-10</span><span class="schedule__dot">•</span><span>wedding ceremony</span></p>
      <p class="schedule__row schedule__row--cont">drinks / dinner / party</p>
      <p class="schedule__row"><span class="schedule__day">8-10</span><span class="schedule__dot">•</span><span>hangover breakfast</span></p>
    </div>
    <p class="line airports">Nearest Airports Valencia &amp; Alicante</p>
    <p class="line more-info">More info will be available soon!</p>
  </section>

</main>
</body>
</html>
```